Professional PowerPoint Template for Data Reports, Presentations

We are a small leadership coaching/consulting firm and would like to update our PowerPoint template that we use with our clients, who are typically mid-senior level company professionals. I've attached a sample Powerpoint as well as our branding guide. The cover page is what needs the most work - just doesn't look current/professional enough. We do want to keep the pages after that clean, with come color but enough space for text and graphics.
Target Market(s)
Senior mgmt and HR executives in small-mid sized companies
Font styles to use
Sans Serif
Requirements
Must have
- Professional
- Clean
- Tied to company color scheme/logo
Nice to have
- Our title pages don't usually have many words on them; we'd like a design that has a lot of color - probably still using mainly our blue but accented with other colors.
- Need simple but smart looking pages after cover with lot of space; mostly we have text on the slides. Currently this is often in bullet point style, but we could probably upgrade the options there.
Should not have
- Anything that looks like a marketing style, as we typically use these with our current clients to share results of data collected, project plans, etc.

```html
<!DOCTYPE html>
<html lang="en">
<head>
<meta charset="utf-8">
<title>Corvane – Presentation Template</title>
<link href="https://fonts.googleapis.com/css2?family=Montserrat:wght@500;600;700;800&family=Arimo:wght@400;700&display=swap" rel="stylesheet">
<style>
  :root {
    --navy: #414f78;
    --navy-deep: #2c3a5c;
    --side-blue: #1f4e7f;
    --orange: #e97d52;
    --green: #80b09b;
    --lavender: #ddd5e8;
    --mist: #eeecea;
    --grey: #e6e6e7;
    --ink: #1d1d22;
    --peach: #f7b49a;
    --mint: #7fcdb4;
    --white: #ffffff;
    --head: "Montserrat", sans-serif;
    --body: "Arimo", sans-serif;
  }
  * { box-sizing: border-box; margin: 0; padding: 0; }
  html, body { width: 1040px; height: 1200px; overflow: hidden; background: var(--white); }
  body { position: relative; font-family: var(--body); color: var(--ink); }

  .slide {
    position: absolute; width: 595px; height: 447px; overflow: hidden;
    background: var(--white); outline: 1.2px solid #222;
    transform: scale(0.8067); transform-origin: 0 0;
  }
  .s-cover { left: 40px; top: 55px; }
  .s-contents { left: 520px; top: 55px; }
  .s-about { left: 40px; top: 415.6px; }
  .s-team { left: 520px; top: 415.6px; }
  .s-picture-left { left: 40px; top: 776.2px; }
  .s-picture-right { left: 520px; top: 776.2px; }

  .abs { position: absolute; }

  /* brand */
  .brand { display: flex; align-items: center; gap: 10px; font-family: var(--head); font-weight: 600; color: var(--ink); letter-spacing: 0.09em; }
  .brand-dot { border: 3px solid var(--ink); border-radius: 50%; }

  /* colour strip */
  .strip { display: flex; height: 6px; }
  .strip span:nth-child(1) { flex: 22; background: var(--navy); }
  .strip span:nth-child(2) { flex: 35; background: var(--orange); }
  .strip span:nth-child(3) { flex: 43; background: var(--green); }
  .strip span:nth-child(4) { flex: 45; background: var(--lavender); }
  .strip span:nth-child(5) { flex: 58; background: var(--mist); }
  .strip.reverse { flex-direction: row-reverse; }

  .heading { font-family: var(--head); font-weight: 800; letter-spacing: 0.12em; }
  .lede { font-size: 14px; color: var(--ink); }
  .copy { font-size: 10px; line-height: 1.2; text-align: justify; color: var(--ink); }
  .footer { position: absolute; left: 0; right: 0; bottom: 4px; text-align: center; font-size: 6px; color: #333; }

  .side-tab { position: absolute; right: 0; top: 0; width: 5px; height: 100%; background: var(--side-blue); }
  .side-tab-label {
    position: absolute; right: 0; top: 30px; width: 26px; height: 90px; background: var(--side-blue);
    color: var(--white); font-family: var(--head); font-size: 9px; font-weight: 600; letter-spacing: 0.1em;
    display: flex; align-items: center; justify-content: center;
  }
  .side-tab-label span { transform: rotate(-90deg); white-space: nowrap; }

  /* cover */
  .cover-band { left: 0; top: 0; width: 595px; height: 17px; background: var(--navy); }
  .cover-brand { right: 75px; top: 70px; font-size: 33px; }
  .cover-brand .brand-dot { width: 34px; height: 34px; }
  .cover-title { right: 75px; top: 140px; font-size: 20px; color: var(--navy); }
  .cover-sub { right: 75px; top: 170px; font-family: var(--head); font-weight: 700; font-size: 14px; letter-spacing: 0.03em; }
  .cover-shapes { left: 0; top: 0; }

  /* contents */
  .contents-title { left: 45px; top: 43px; font-size: 20px; color: var(--navy); }
  .contents-strip { left: 183px; top: 50px; width: 205px; }
  .contents-lede { left: 45px; top: 80px; }
  .topic { position: absolute; width: 255px; }
  .topic-num {
    position: absolute; left: 0; top: 0; width: 32px; height: 32px; border: 3px solid var(--navy);
    background: var(--white); font-family: var(--head); font-weight: 700; font-size: 19px; color: var(--navy);
    display: flex; align-items: center; justify-content: center;
  }
  .topic-back { position: absolute; left: -4px; top: -4px; width: 32px; height: 32px; }
  .topic h3 { position: absolute; left: 46px; top: -5px; font-size: 10px; font-weight: 700; text-decoration: underline; }
  .topic .copy { position: absolute; left: 46px; top: 9px; width: 201px; font-size: 9.6px; }
  .topic-bar { position: absolute; left: 0; width: 75px; height: 12px; background: var(--navy); border-bottom: 4px solid var(--navy-deep); }

  /* about */
  .about-panel { left: 0; top: 0; width: 250px; height: 447px; background: var(--orange); }
  .about-line-a { left: 250px; top: 0; width: 8px; height: 447px; background: var(--green); }
  .about-line-b { left: 258px; top: 0; width: 5px; height: 447px; background: var(--lavender); }
  .about-brand { left: 55px; top: 76px; font-size: 26px; }
  .about-brand .brand-dot { width: 28px; height: 28px; }
  .about-mat { left: 38px; top: 130px; width: 290px; height: 272px; background: var(--mist); }
  .about-photo { left: 50px; top: 120px; width: 287px; height: 272px; background: radial-gradient(circle at 60% 45%, #fcc7ae, var(--peach) 70%, #f3a98c); }
  .about-title { left: 358px; top: 143px; font-size: 20px; color: var(--orange); }
  .about-lede { left: 358px; top: 172px; }
  .about-strip { left: 360px; top: 199px; width: 178px; }
  .about-copy { left: 362px; top: 232px; width: 179px; }

  /* team */
  .team-title { left: 0; width: 585px; top: 45px; text-align: center; font-size: 19px; color: var(--ink); }
  .team-lede { left: 0; width: 585px; top: 73px; text-align: center; font-size: 13px; }
  .team-strip { left: 192px; top: 103px; width: 205px; }
  .member { position: absolute; top: 146px; width: 130px; text-align: center; }
  .member-back { position: absolute; left: 14px; top: -4px; width: 92px; height: 92px; }
  .member-photo { position: absolute; left: 18px; top: 0; width: 95px; height: 95px; border: 3px solid var(--navy-deep); background: linear-gradient(160deg, #f2f2f2, #c8c8c8); }
  .member h3 { position: absolute; left: 0; width: 130px; top: 107px; font-size: 9.5px; font-weight: 700; text-decoration: underline; }
  .member .copy { position: absolute; left: 6px; width: 118px; top: 124px; text-align: center; font-size: 9.5px; }
  .member-links { position: absolute; left: 0; width: 130px; top: 192px; display: flex; justify-content: center; gap: 4px; }
  .member-links i { display: block; width: 11px; height: 11px; background: var(--ink); border-radius: 50%; }

  /* picture slides */
  .pic-field { top: 0; width: 260px; height: 447px; background: var(--green); }
  .pic-rail { width: 25px; background: var(--navy); }
  .pic-thread { width: 8px; background: var(--lavender); }
  .pic-photo { top: 70px; width: 263px; height: 317px; background: linear-gradient(150deg, #93dcc4, var(--mint) 45%, #5fae96); }
  .pic-title { font-size: 19px; line-height: 28px; letter-spacing: 0.12em; }
  .pic-title .a { color: var(--green); display: block; }
  .pic-title .b { color: var(--navy); display: block; }
  .pic-copy { top: 172px; width: 177px; }
</style>
</head>
<body>

<!-- Cover -->
<section class="slide s-cover">
  <svg class="abs cover-shapes" width="595" height="447" viewBox="0 0 595 447" aria-hidden="true">
    <polygon points="0,125 332,447 0,447" fill="var(--grey)"/>
    <polygon points="155,273 378,356 294,412" fill="var(--green)"/>
    <polygon points="265,312 527,262 378,356" fill="var(--orange)"/>
    <polygon points="595,220 595,447 300,447 378,356" fill="var(--navy)" stroke="var(--white)" stroke-width="3" stroke-linejoin="miter"/>
  </svg>
  <div class="abs cover-band"></div>
  <div class="abs brand cover-brand"><span class="brand-dot"></span>CORVANE</div>
  <div class="abs heading cover-title">TITLE TEXT HERE</div>
  <div class="abs cover-sub">SUBTITLE TEXT HERE</div>
</section>

<!-- Contents -->
<section class="slide s-contents">
  <div class="abs heading contents-title">CONTENTS</div>
  <div class="abs strip contents-strip"><span></span><span></span><span></span><span></span><span></span></div>
  <p class="abs lede contents-lede">Lorem ipsum dolor sit amet, consectetuer adipiscing elit</p>

  <div class="topic-bar" style="top:170px"></div>
  <div class="topic-bar" style="top:262px"></div>
  <div class="topic-bar" style="top:360px"></div>

  <div class="topic" style="left:42px; top:133px">
    <div class="topic-back" style="background:var(--green)"></div>
    <div class="topic-num">1</div>
    <h3>About Us</h3>
    <p class="copy">Lorem ipsum dolor sit amet, consectetuer adipiscing elit, sed diam nonummy nibh euismod tincidunt ut laoreet dolore magna aliquam erat volutpat.</p>
  </div>
  <div class="topic" style="left:42px; top:224px">
    <div class="topic-back" style="background:var(--orange)"></div>
    <div class="topic-num">2</div>
    <h3>Our Team</h3>
    <p class="copy">Lorem ipsum dolor sit amet, consectetuer adipiscing elit, sed diam nonummy nibh euismod tincidunt ut laoreet dolore magna aliquam erat volutpat.</p>
  </div>
  <div class="topic" style="left:42px; top:322px">
    <div class="topic-back" style="background:var(--lavender)"></div>
    <div class="topic-num">3</div>
    <h3>Our Goals</h3>
    <p class="copy">Lorem ipsum dolor sit amet, consectetuer adipiscing elit, sed diam nonummy nibh euismod tincidunt ut laoreet dolore magna aliquam erat volutpat.</p>
  </div>
  <div class="topic" style="left:312px; top:133px">
    <div class="topic-back" style="background:var(--lavender)"></div>
    <div class="topic-num">4</div>
    <h3>Contents</h3>
    <p class="copy">Lorem ipsum dolor sit amet, consectetuer adipiscing elit, sed diam nonummy nibh euismod tincidunt ut laoreet dolore magna aliquam erat volutpat.</p>
  </div>
  <div class="topic" style="left:312px; top:224px">
    <div class="topic-back" style="background:var(--green)"></div>
    <div class="topic-num">5</div>
    <h3>Our Progress</h3>
    <p class="copy">Lorem ipsum dolor sit amet, consectetuer adipiscing elit, sed diam nonummy nibh euismod tincidunt ut laoreet dolore magna aliquam erat volutpat.</p>
  </div>
  <div class="topic" style="left:312px; top:324px">
    <div class="topic-back" style="background:var(--orange)"></div>
    <div class="topic-num">6</div>
    <h3>Our Target</h3>
    <p class="copy">Lorem ipsum dolor sit amet, consectetuer adipiscing elit, sed diam nonummy nibh euismod tincidunt ut laoreet dolore magna aliquam erat volutpat.</p>
  </div>

  <div class="side-tab"></div>
  <div class="side-tab-label"><span>CORVANE</span></div>
  <p class="footer">© Corvane Company www.corvanecompany.com 555-010-0199</p>
</section>

<!-- About -->
<section class="slide s-about">
  <div class="abs about-panel"></div>
  <div class="abs about-line-a"></div>
  <div class="abs about-line-b"></div>
  <div class="abs brand about-brand"><span class="brand-dot"></span>CORVANE</div>
  <div class="abs about-mat"></div>
  <div class="abs about-photo" role="img" aria-label="Photo of a peach telephone handset resting on a peach surface"></div>
  <div class="abs heading about-title">ABOUT US</div>
  <p class="abs lede about-lede">Lorem ipsum dolor sit amet.</p>
  <div class="abs strip about-strip"><span></span><span></span><span></span><span></span><span></span></div>
  <p class="abs copy about-copy">Lorem ipsum dolor sit amet, ut qui tale interesset, pri eu zril solet altera. Quo graeco detracto indoctum ex, vocent oportere usu no, at cetero corpora forensibus per. Eos suas equidem an, per quando nullam rationibus cu, sit solet dicunt habemus ne. Ius vivendum delicatissimi at, ut nec graeci postulant, nec cu sonet essent.</p>
</section>

<!-- Team -->
<section class="slide s-team">
  <div class="abs heading team-title">MEET OUR TEAM</div>
  <p class="abs team-lede">Lorem ipsum dolor sit amet.</p>
  <div class="abs strip team-strip"><span></span><span></span><span></span><span></span><span></span></div>

  <div class="member" style="left:56px">
    <div class="member-back" style="background:var(--green)"></div>
    <div class="member-photo" role="img" aria-label="Black and white portrait of a team member seated on a chair"></div>
    <h3>Name Here</h3>
    <p class="copy">Lorem ipsum dolor sit amet, consectetuer adipiscing elit, sed diam nonummy nibh euismod tincidunt ut laoreet dolore.</p>
    <div class="member-links"><i></i><i></i>
      <svg width="13" height="11" viewBox="0 0 13 11" aria-label="Email"><rect x="0.5" y="0.5" width="12" height="10" fill="var(--ink)"/><path d="M1 1.5 L6.5 6 L12 1.5" stroke="var(--white)" stroke-width="1.2" fill="none"/></svg>
    </div>
  </div>
  <div class="member" style="left:225px">
    <div class="member-back" style="background:var(--orange)"></div>
    <div class="member-photo" role="img" aria-label="Black and white portrait of a team member"></div>
    <h3>Name Here</h3>
    <p class="copy">Lorem ipsum dolor sit amet, consectetuer adipiscing elit, sed diam nonummy nibh euismod tincidunt ut laoreet dolore.</p>
    <div class="member-links"><i></i><i></i>
      <svg width="13" height="11" viewBox="0 0 13 11" aria-label="Email"><rect x="0.5" y="0.5" width="12" height="10" fill="var(--ink)"/><path d="M1 1.5 L6.5 6 L12 1.5" stroke="var(--white)" stroke-width="1.2" fill="none"/></svg>
    </div>
  </div>
  <div class="member" style="left:394px">
    <div class="member-back" style="background:var(--navy)"></div>
    <div class="member-photo" role="img" aria-label="Black and white portrait of a team member"></div>
    <h3>Name Here</h3>
    <p class="copy">Lorem ipsum dolor sit amet, consectetuer adipiscing elit, sed diam nonummy nibh euismod tincidunt ut laoreet dolore.</p>
    <div class="member-links"><i></i><i></i>
      <svg width="13" height="11" viewBox="0 0 13 11" aria-label="Email"><rect x="0.5" y="0.5" width="12" height="10" fill="var(--ink)"/><path d="M1 1.5 L6.5 6 L12 1.5" stroke="var(--white)" stroke-width="1.2" fill="none"/></svg>
    </div>
  </div>

  <div class="side-tab"></div>
  <div class="side-tab-label"><span>CORVANE</span></div>
  <p class="footer">© Corvane Company www.corvanecompany.com 555-010-0199</p>
</section>

<!-- One picture slide, image right -->
<section class="slide s-picture-left">
  <div class="abs pic-field" style="left:335px"></div>
  <div class="abs pic-thread" style="left:300px; top:0; height:70px"></div>
  <div class="abs pic-thread" style="left:300px; top:387px; height:60px"></div>
  <div class="abs pic-rail" style="left:308px; top:0; height:70px"></div>
  <div class="abs pic-rail" style="left:308px; top:387px; height:60px"></div>
  <div class="abs pic-photo" style="left:265px" role="img" aria-label="Photo of crumpled mint green fabric"></div>
  <div class="abs heading pic-title" style="right:352px; top:70px; text-align:right"><span class="a">ONE PICTURE</span><span class="b">SLIDE</span></div>
  <div class="abs strip reverse" style="left:68px; top:142px; width:177px"><span></span><span></span><span></span><span></span><span></span></div>
  <p class="abs copy pic-copy" style="left:68px; text-align-last:right">Lorem ipsum dolor sit amet, ut qui tale interesset, pri eu zril solet altera. Quo graeco detracto indoctum ex, vocent oportere usu no, at cetero corpora forensibus per. Eos suas equidem an, per quando nullam rationibus cu, sit solet dicunt habemus ne. Ius vivendum delicatissimi at, ut nec graeci postulant, nec cu sonet essent.</p>
</section>

<!-- One picture slide, image left -->
<section class="slide s-picture-right">
  <div class="abs pic-field" style="left:0; width:262px"></div>
  <div class="abs pic-rail" style="left:262px; top:0; height:70px"></div>
  <div class="abs pic-rail" style="left:262px; top:387px; height:60px"></div>
  <div class="abs pic-thread" style="left:287px; top:0; height:70px"></div>
  <div class="abs pic-thread" style="left:287px; top:387px; height:60px"></div>
  <div class="abs pic-photo" style="left:68px" role="img" aria-label="Photo of crumpled mint green fabric"></div>
  <div class="abs heading pic-title" style="left:365px; top:70px"><span class="a">ONE PICTURE</span><span class="b">SLIDE</span></div>
  <div class="abs strip reverse" style="left:366px; top:142px; width:178px"><span></span><span></span><span></span><span></span><span></span></div>
  <p class="abs copy pic-copy" style="left:366px">Lorem ipsum dolor sit amet, ut qui tale interesset, pri eu zril solet altera. Quo graeco detracto indoctum ex, vocent oportere usu no, at cetero corpora forensibus per. Eos suas equidem an, per quando nullam rationibus cu, sit solet dicunt habemus ne. Ius vivendum delicatissimi at, ut nec graeci postulant, nec cu sonet essent.</p>
</section>

</body>
</html>
```